Website of KESTRAVO | The Amber Horizon Company

I need a simple and effective website where users can quickly understand what the company is all about and the added value of the services provided. The site should be attractive and modern, based on the logo and on the corporate slideshow attached.

Target Market(s)

Public and Private organizations from maritime security and defense, looking for solutions in the field s of digital transformation and cybersecurity.

Coding

Coded - Design and coding required

Requirements
Must have
• A form through which can contact the company by email to request additional information.

```html
<!DOCTYPE html>
<html lang="en">
<head>
<meta charset="utf-8">
<title>KESTRAVO | The Amber Horizon Company</title>
<link href="https://fonts.googleapis.com/css2?family=Montserrat:wght@400;500;600;700&display=swap" rel="stylesheet">
<style>
  :root{
    --blue:#2a93d5;
    --blue-light:#4aa8dd;
    --ink:#111;
    --black:#000;
    --grey:#6b6b6b;
    --white:#fff;
    --sea-dark:#3b5a6e;
    --sea-mid:#7c97a6;
  }
  *{margin:0;padding:0;box-sizing:border-box}
  html,body{width:1200px;height:3357px;overflow:hidden;background:var(--white)}
  body{font-family:'Montserrat',sans-serif;color:var(--ink);position:relative}
  .abs{position:absolute}

  /* Hero */
  .hero{left:0;top:0;width:1200px;height:597px;border-radius:0 65px 0 110px;overflow:hidden;
    background:linear-gradient(160deg,#c9b69a 0%,#8ea2ae 30%,var(--sea-mid) 55%,var(--sea-dark) 100%)}
  .brand{font-weight:700;color:var(--ink);display:flex;align-items:center;white-space:nowrap}
  .brand-dot{border-radius:50%;background:var(--blue);flex:none}
  .header-brand{left:115px;top:28px;font-size:34px;letter-spacing:1px;gap:12px}
  .header-brand .brand-dot{width:30px;height:30px}
  .nav{top:42px;left:498px;width:640px;display:flex;font-size:16px;font-weight:500;white-space:nowrap}
  .nav a{color:var(--ink);text-decoration:none;padding:3px 12px;line-height:20px}
  .nav a.active{background:var(--blue);color:var(--white);border-radius:3px;margin-right:11px}
  .nav a + a{margin-right:11px}
  .hero-card{left:117px;top:141px;width:358px;height:349px}
  .hero-title{left:142px;top:190px;width:320px;color:var(--white);font-weight:600;font-size:24px;line-height:32px}
  .hero-sub{left:145px;top:300px;width:250px;color:var(--white);font-size:14px;line-height:24px}
  .btn{display:inline-flex;align-items:center;justify-content:center;background:var(--blue);color:var(--white);
    font-weight:500;border-radius:30px;text-decoration:none;border:0;font-family:inherit}
  .hero-btn{left:142px;top:384px;width:134px;height:42px;font-size:16px}

  /* Section headings */
  .heading{font-size:44px;font-weight:400;letter-spacing:1px;text-align:center;width:1200px;left:0}
  .heading b{font-weight:700}
  .rule{height:3px;width:40px;background:var(--blue);left:561px}

  /* About */
  .about-title{left:115px;top:730px;font-size:43px;font-weight:700;letter-spacing:1px}
  .about-title span{font-weight:400;color:var(--blue)}
  .about-rule{left:115px;top:794px;width:75px;height:3px;background:var(--blue)}
  .about-text{left:115px;top:825px;width:470px;font-size:16px;line-height:30px;color:#333}
  .about-btn{left:116px;top:1027px;width:150px;height:46px;font-size:18px}
  .about-media{left:640px;top:683px;width:526px;height:436px}

  /* Services */
  .services{left:0;top:1214px;width:1200px;height:725px;
    background:linear-gradient(180deg,#3897d4 0%,#5aa9d8 45%,#3b8fc6 100%)}
  .services-rule{top:1365px;background:var(--white)}
  .card{top:1411px;width:320px;height:409px;border-radius:26px 46px 46px 46px;background:var(--black);overflow:hidden}
  .card.alt{background:var(--blue-light)}
  .card-media{position:absolute;left:8px;top:8px;width:304px;height:196px;border-radius:0 40px 40px 40px}
  .card h3{position:absolute;left:29px;top:222px;color:var(--white);font-size:18px;font-weight:600;white-space:nowrap}
  .card p{position:absolute;left:29px;top:262px;width:262px;color:var(--white);font-size:13.5px;line-height:20px}
  .card-arrow{position:absolute;right:16px;bottom:20px;width:46px;height:46px;border-radius:50%;background:var(--blue-light)}
  .card.alt .card-arrow{background:var(--blue)}

  /* Why choose */
  .why-rule{top:2079px}
  .why-links{left:220px;top:2140px}
  .feature{top:2140px;width:250px;text-align:center}
  .badge{width:128px;height:116px;margin:0 auto;display:block}
  .feature h4{margin-top:20px;font-size:18px;font-weight:600}
  .feature p{margin-top:12px;font-size:16px;line-height:24px;color:var(--grey)}

  /* Collaborate */
  .collab{left:0;top:2508px;width:1200px;height:411px;background:#0c0c0c;border-radius:0 150px 0 150px}
  .collab-rule{top:2650px}
  .collab-sub{left:0;width:1200px;top:2676px;text-align:center;color:var(--white);font-size:40px;font-weight:500}
  .collab-text{left:170px;width:860px;top:2750px;text-align:center;color:var(--white);font-size:19px;line-height:35px}
  .contact-form{left:190px;top:2840px;width:820px;display:flex;gap:12px}
  .contact-form input{height:44px;border:1px solid rgba(255,255,255,.45);background:rgba(255,255,255,.08);
    color:var(--white);border-radius:22px;padding:0 18px;font:14px 'Montserrat',sans-serif}
  .contact-form input::placeholder{color:rgba(255,255,255,.7)}
  .field-name{width:180px}
  .field-email{width:210px}
  .field-message{flex:1}
  .form-btn{width:120px;height:44px;font-size:15px}

  /* Footer */
  .footer-brand{left:0;width:1200px;top:2990px;justify-content:center;font-size:62px;letter-spacing:1px;gap:18px}
  .footer-brand .brand-dot{width:52px;height:52px}
  .footer-nav{left:0;width:1200px;top:3118px;display:flex;justify-content:center;gap:42px;font-size:19px;white-space:nowrap}
  .footer-nav a{color:var(--ink);text-decoration:none}
  .social{left:0;width:1200px;top:3192px;display:flex;justify-content:center;gap:6px}
  .social span{width:41px;height:41px;border:2px solid var(--ink);border-radius:50%}
  .social span.on{border-color:var(--blue)}
  .copy{left:0;width:1200px;top:3292px;text-align:center;font-size:16px}
</style>
</head>
<body>

<header class="abs hero" role="img" aria-label="Photo of a loaded container ship sailing past a city skyline at dusk"></header>
<div class="abs brand header-brand"><span class="brand-dot"></span>KESTRAVO</div>
<nav class="abs nav">
  <a class="active" href="#">Home</a><a href="#">About Us</a><a href="#">Our Services</a><a href="#">Why Choose Us</a><a href="#">Contact us</a>
</nav>
<svg class="abs hero-card" viewBox="0 0 358 349">
  <path d="M30 0 H240 A118 118 0 0 1 358 118 V349 H60 A60 60 0 0 1 0 289 V30 A30 30 0 0 1 30 0Z" fill="#3a9cdc" opacity=".92"/>
  <path d="M181 240 A90 90 0 0 1 358 200 V349 H270 A90 90 0 0 1 181 260Z" fill="#000"/>
</svg>
<h1 class="abs hero-title">Innovative Solutions For Maritime Security And Defense</h1>
<p class="abs hero-sub">Empowering Organizations With Cutting Edge Consulting And Technology</p>
<a class="abs btn hero-btn" href="#">Get Started</a>

<section class="about">
  <h2 class="abs about-title">ABOUT <span>US</span></h2>
  <div class="abs about-rule"></div>
  <p class="abs about-text">KESTRAVO specializes in delivering innovative solutions for maritime security and defense in the fields of digital transformation and cybersecurity.By combining unparalleled expertise withstrategic partnerships, we empowerorganizations to overcome challenges, seizeopportunities, and achieve success.</p>
  <a class="abs btn about-btn" href="#">Read More</a>
  <svg class="abs about-media" viewBox="0 0 526 436">
    <defs><radialGradient id="droneSky" cx=".5" cy=".5" r=".6"><stop offset="0" stop-color="#4f8fa3"/><stop offset="1" stop-color="#1d3f52"/></radialGradient></defs>
    <path d="M0 0 H310 V436 H110 A110 110 0 0 1 0 326Z" fill="#4aa8de"/>
    <path d="M0 0 H180 A140 140 0 0 0 90 40 H0Z" fill="#2a8fd0"/>
    <circle cx="308" cy="218" r="216" fill="url(#droneSky)" role="img" aria-label="Photo of a surveillance drone flying over a lit city at night"/>
  </svg>
</section>

<section class="abs services" role="img" aria-label="Blue toned photo of naval ships at sea"></section>
<h2 class="abs heading" style="top:1300px;color:#fff">OUR <b>SERVICES</b></h2>
<div class="abs rule services-rule"></div>

<article class="abs card" style="left:112px">
  <div class="card-media" role="img" aria-label="Photo of a person reviewing data charts on a laptop" style="background:linear-gradient(135deg,#dfe8ef,#7ea6c4 60%,#2d5d8c)"></div>
  <h3>STRATEGY AND DESIGN</h3>
  <p>Services focused on helping clients define their vision, assess their needs, and design innovative solutions, including</p>
  <svg class="card-arrow" viewBox="0 0 46 46"><circle cx="23" cy="23" r="10" fill="#fff"/><path d="M21 18l5 5-5 5" stroke="#4aa8dd" stroke-width="2.5" fill="none"/></svg>
</article>
<article class="abs card alt" style="left:444px">
  <div class="card-media" role="img" aria-label="Photo of a team reviewing printed reports on a table" style="background:linear-gradient(135deg,#3a3a3a,#8b8378 55%,#d9d4cc)"></div>
  <h3>STRATEGIC ASSESSMENTS</h3>
  <p>conducting market surveys, identifying challenges, and uncovering opportunities.</p>
  <svg class="card-arrow" viewBox="0 0 46 46"><circle cx="23" cy="23" r="10" fill="#fff"/><path d="M21 18l5 5-5 5" stroke="#2a93d5" stroke-width="2.5" fill="none"/></svg>
</article>
<article class="abs card" style="left:776px">
  <div class="card-media" role="img" aria-label="Illustration of a glowing path leading to a location pin" style="background:linear-gradient(135deg,#1b4a5c,#2f6f80 50%,#7a5a2c)"></div>
  <h3>STRATEGIC ROADMAPS</h3>
  <p>Developing highlevel plans that outline the steps, priorities, and resources needed to achieve the organization's vision</p>
  <svg class="card-arrow" viewBox="0 0 46 46"><circle cx="23" cy="23" r="10" fill="#fff"/><path d="M21 18l5 5-5 5" stroke="#4aa8dd" stroke-width="2.5" fill="none"/></svg>
</article>

<section class="why">
  <h2 class="abs heading" style="top:2012px">WHY <b style="color:var(--blue)">CHOOSE US</b></h2>
  <div class="abs rule why-rule"></div>
  <svg class="abs why-links" width="780" height="120" viewBox="0 0 780 120">
    <path d="M60 90 Q130 110 210 70 M255 45 Q350 -10 440 50 M510 85 Q580 110 660 65" stroke="#bbb" stroke-width="1.5" stroke-dasharray="6 5" fill="none"/>
  </svg>

  <div class="abs feature" style="left:96px">
    <svg class="badge" viewBox="0 0 128 116"><path d="M10 0 H64 A58 58 0 1 1 28 104 Q14 60 10 0Z" fill="#2a93d5"/><circle cx="68" cy="58" r="44" fill="#fff"/>
      <g stroke="#2a6f9e" stroke-width="2" fill="none"><circle cx="68" cy="46" r="8"/><circle cx="52" cy="54" r="6"/><circle cx="84" cy="54" r="6"/><path d="M54 78c0-10 6-16 14-16s14 6 14 16M40 76c0-8 5-12 12-12M96 76c0-8-5-12-12-12"/></g></svg>
    <h4>Expert Team</h4>
    <p>Decades of combined worldwide experience in maritime security, defense, digital transformation,</p>
  </div>
  <div class="abs feature" style="left:351px">
    <svg class="badge" viewBox="0 0 128 116"><path d="M10 0 H64 A58 58 0 1 1 28 104 Q14 60 10 0Z" fill="#2a93d5"/><circle cx="68" cy="58" r="44" fill="#fff"/>
      <g stroke="#2a6f9e" stroke-width="2" fill="none"><path d="M42 56l14-12 12 6 12-6 14 12-18 18-10-8-8 8z"/><path d="M60 38l-3-6M68 34v-6M76 38l3-6"/></g></svg>
    <h4>Proven Partnerships</h4>
    <p>Access to state-of-the-art knowledge, practices and technology through key alliances.</p>
  </div>
  <div class="abs feature" style="left:607px">
    <svg class="badge" viewBox="0 0 128 116"><path d="M10 0 H64 A58 58 0 1 1 28 104 Q14 60 10 0Z" fill="#2a93d5"/><circle cx="68" cy="58" r="44" fill="#fff"/>
      <g stroke="#2a6f9e" stroke-width="2" fill="none"><path d="M60 62a12 12 0 1 1 16 0v6h-16z"/><path d="M62 74h12M64 79h8M68 30v-5M52 38l-4-4M84 38l4-4"/></g></svg>
    <h4>Tailored Strategies</h4>
    <p>Customized designs addressing unique organizational needs.</p>
  </div>
  <div class="abs feature" style="left:863px">
    <svg class="badge" viewBox="0 0 128 116"><path d="M10 0 H64 A58 58 0 1 1 28 104 Q14 60 10 0Z" fill="#2a93d5"/><circle cx="68" cy="58" r="44" fill="#fff"/>
      <g stroke="#2a6f9e" stroke-width="2" fill="none"><circle cx="68" cy="54" r="18"/><path d="M50 54h36M68 36c-8 10-8 26 0 36M68 36c8 10 8 26 0 36M62 76h12M64 81h8"/></g></svg>
    <h4>Innovative Solutions</h4>
    <p>Decades of combined worldwide experience in maritime security, defense, digital transformation,</p>
  </div>
</section>

<section class="abs collab"></section>
<h2 class="abs heading" style="top:2588px;color:#fff">LET'S <b>COLLABORATE</b></h2>
<div class="abs rule collab-rule"></div>
<p class="abs collab-sub">Ready to innovate together?</p>
<p class="abs collab-text">KESTRAVO is here to help you navigate challenges and unlock new opportunities for maritime security and defense with digital transformation and cybersecurity solutions.</p>
<form class="abs contact-form" action="mailto:info@kestravo-example.com" method="post" enctype="text/plain">
  <input class="field-name" type="text" name="name" placeholder="Your name" aria-label="Your name">
  <input class="field-email" type="email" name="email" placeholder="Your email" aria-label="Your email">
  <input class="field-message" type="text" name="message" placeholder="How can we help?" aria-label="Message">
  <button class="btn form-btn" type="submit">Send</button>
</form>

<footer>
  <div class="abs brand footer-brand"><span class="brand-dot"></span>KESTRAVO</div>
  <nav class="abs footer-nav"><a href="#">Home</a><a href="#">About Us</a><a href="#">Our Services</a><a href="#">Why Choose Us</a><a href="#">Contact us</a></nav>
  <div class="abs social" aria-label="Social links"><span></span><span></span><span class="on"></span><span></span><span></span></div>
  <p class="abs copy">Copyrights 2025 Company Name All Rights Reserved</p>
</footer>

</body>
</html>
```